Quorvex business card design

create modern and tech looking business card that is clean but effectively communciates that we are a cloud communications company.
Should have at minimum:
Employee Name
Postion
Phone Number
Email
website
create modern and tech looking business card that is clean but effectively communciates that we are a cloud communications company. We have two logo color schemes (attached) so would like to see designs both ways
Should have at minimum:
Employee Name
Postion
Phone Number
Email
website

```html
<!DOCTYPE html>
<html lang="en">
<head>
<meta charset="UTF-8">
<title>Quorvex Business Card</title>
<link href="https://fonts.googleapis.com/css2?family=Open+Sans:wght@400;600;700&display=swap" rel="stylesheet">
<style>
  :root {
    --bg: #2a2b2e;
    --cyan: #2bbde0;
    --cyan-light: #45e0f0;
    --purple: #6a2fa0;
    --purple-text: #6b2fa3;
    --ink: #4a4a4c;
    --white: #ffffff;
    --rule: #c9c9cc;
  }
  * { margin: 0; padding: 0; box-sizing: border-box; }
  html, body { width: 1200px; height: 840px; overflow: hidden; }
  body {
    background: var(--bg);
    font-family: "Open Sans", Arial, sans-serif;
    position: relative;
  }
  .card {
    position: absolute;
    width: 560px;
    height: 320px;
    overflow: hidden;
  }
  /* Back side */
  .card-back {
    left: 120px;
    top: 70px;
    background: linear-gradient(135deg, var(--cyan-light) 0%, var(--cyan) 60%, #25b2d8 100%);
    color: var(--white);
  }
  .back-brand {
    position: absolute;
    left: 0; right: 0; top: 118px;
    display: flex;
    align-items: center;
    justify-content: center;
    gap: 14px;
  }
  .back-brand .mark {
    width: 34px; height: 34px;
    border-radius: 50%;
    background: var(--white);
  }
  .back-brand .name {
    font-size: 40px;
    font-weight: 700;
    letter-spacing: 2px;
    color: var(--white);
  }
  .back-web {
    position: absolute;
    left: 0; right: 0; bottom: 34px;
    text-align: center;
    font-size: 13px;
    letter-spacing: 6px;
    color: var(--white);
  }
  /* Front side */
  .card-front {
    left: 520px;
    top: 450px;
    background: var(--white);
  }
  .front-waves { position: absolute; inset: 0; }
  .front-brand {
    position: absolute;
    left: 58px;
    top: 150px;
    display: flex;
    align-items: center;
    gap: 12px;
  }
  .front-brand .mark {
    width: 26px; height: 26px;
    background: var(--purple);
  }
  .front-brand .name {
    font-size: 34px;
    font-weight: 700;
    letter-spacing: 1px;
    color: var(--ink);
  }
  .divider {
    position: absolute;
    left: 320px;
    top: 80px;
    width: 1px;
    height: 120px;
    background: var(--rule);
  }
  .contact {
    position: absolute;
    left: 340px;
    top: 86px;
  }
  .contact .person {
    font-size: 15px;
    font-weight: 700;
    color: var(--purple-text);
    line-height: 1.2;
  }
  .contact .role {
    font-size: 14px;
    color: var(--cyan);
    line-height: 1.3;
    margin-bottom: 4px;
  }
  .contact ul { list-style: none; }
  .contact li {
    display: flex;
    align-items: center;
    gap: 8px;
    font-size: 13px;
    color: var(--ink);
    line-height: 1.45;
  }
  .contact svg { width: 11px; height: 11px; fill: var(--purple); flex: none; }
</style>
</head>
<body>

  <section class="card card-back" aria-label="Card back">
    <div class="back-brand">
      <span class="mark"></span>
      <span class="name">QUORVEX</span>
    </div>
    <div class="back-web">www.quorvex.com</div>
  </section>

  <section class="card card-front" aria-label="Card front">
    <svg class="front-waves" viewBox="0 0 560 320" preserveAspectRatio="none" aria-hidden="true">
      <path d="M0 70 C80 40 200 20 330 0 L0 0 Z" fill="var(--purple)"/>
      <path d="M0 70 C20 90 30 140 40 180 C20 140 10 110 0 100 Z" fill="var(--purple)"/>
      <path d="M0 320 L0 300 C160 300 380 260 560 140 L560 320 Z" fill="var(--cyan)"/>
      <path d="M0 300 C160 300 380 260 560 140 L560 160 C390 272 180 310 0 312 Z" fill="var(--white)" opacity="0.0"/>
    </svg>

    <div class="front-brand">
      <span class="mark"></span>
      <span class="name">QUORVEX</span>
    </div>

    <div class="divider"></div>

    <div class="contact">
      <p class="person">MAREN HOLT</p>
      <p class="role">CEO/FOUNDER</p>
      <ul>
        <li><svg viewBox="0 0 24 24"><path d="M6.6 10.8a15 15 0 0 0 6.6 6.6l2.2-2.2c.3-.3.7-.4 1-.2 1.1.4 2.3.6 3.6.6.6 0 1 .4 1 1V20c0 .6-.4 1-1 1A17 17 0 0 1 3 4c0-.6.4-1 1-1h3.5c.6 0 1 .4 1 1 0 1.3.2 2.5.6 3.6.1.3 0 .7-.2 1z"/></svg>555 014 7321</li>
        <li><svg viewBox="0 0 24 24"><path d="M2 5h20v14H2z M2 5l10 8 10-8" /></svg>hello@quorvex.com</li>
        <li><svg viewBox="0 0 24 24"><circle cx="12" cy="12" r="10"/></svg>www.quorvex.com</li>
      </ul>
    </div>
  </section>

</body>
</html>
```